Design some Business Cards for Kestrel Data Works

I would like a nicely designed business card template for my re-branded business, 'Kestrel Data Works'.

I would like it to be a standard landscape design to fit on 88.5*50mm PVC plastic cards:

I've attached our business logo files, if the design could match their style and color scheme while making good aesthetic use of the transparent plastic medium they will be printed on that would be fantastic.

```html
<!DOCTYPE html>
<html lang="en">
<head>
<meta charset="utf-8">
<title>Kestrel Data Works – Business Card</title>
<link rel="stylesheet" href="https://fonts.googleapis.com/css2?family=Source+Sans+3:wght@400;600;700&display=swap">
<style>
  :root {
    --backdrop: #2a2a2c;
    --frost-top: rgba(236, 238, 240, 0.92);
    --frost-bottom: rgba(200, 204, 208, 0.88);
    --navy: #2d3a88;
    --lime: #8cc63f;
    --lime-dark: #6fa52c;
    --brand-blue: #1f7fb8;
    --ink-light: #ffffff;
    --ink-muted: #4b5a2a;
  }
  * { margin: 0; padding: 0; box-sizing: border-box; }
  html, body {
    width: 1200px; height: 800px; overflow: hidden;
    background: var(--backdrop);
    font-family: "Source Sans 3", "Myriad Pro", sans-serif;
  }
  .card {
    position: absolute; left: 150px; top: 146px;
    width: 900px; height: 508px;
    border-radius: 26px;
    background: linear-gradient(160deg, var(--frost-top), var(--frost-bottom));
    box-shadow: inset 0 0 0 2px rgba(255,255,255,0.6), 0 18px 40px rgba(0,0,0,0.45);
    overflow: hidden;
  }
  .brand {
    position: absolute; left: 0; right: 0; top: 120px;
    display: flex; align-items: center; justify-content: center; gap: 18px;
    padding-left: 120px;
  }
  .brand-dot {
    width: 34px; height: 34px; border-radius: 50%;
    background: var(--lime);
  }
  .brand-name {
    font-size: 50px; font-weight: 700; color: var(--brand-blue);
    letter-spacing: -0.5px;
  }
  .name-band {
    position: absolute; left: 0; right: 0; top: 336px; height: 92px;
    background: linear-gradient(180deg, var(--lime), var(--lime-dark));
  }
  .holder {
    position: absolute; left: 580px; top: 344px; width: 300px;
    text-align: center;
  }
  .holder-name { font-size: 32px; font-weight: 400; color: var(--ink-light); line-height: 1.1; }
  .holder-role { font-size: 22px; font-weight: 400; color: var(--ink-muted); line-height: 1.3; }
  .contact-panel {
    position: absolute; left: -6px; top: 226px;
    width: 536px; height: 190px;
    background: var(--navy);
    border: 5px solid var(--lime);
    border-radius: 0 42px 42px 0;
    padding: 24px 0 0 90px;
  }
  .contact-list { list-style: none; }
  .contact-list li {
    display: flex; align-items: center; gap: 16px;
    font-size: 23px; color: var(--ink-light); line-height: 34px;
  }
  .contact-list svg { width: 18px; height: 18px; flex: none; }
</style>
</head>
<body>
  <section class="card" aria-label="Business card">
    <div class="brand">
      <span class="brand-dot"></span>
      <span class="brand-name">Kestrel Data Works</span>
    </div>

    <div class="name-band"></div>

    <div class="contact-panel">
      <ul class="contact-list">
        <li>
          <svg viewBox="0 0 24 24" aria-hidden="true"><path fill="#fff" d="M6.6 10.8a15 15 0 0 0 6.6 6.6l2.2-2.2a1 1 0 0 1 1-.25 11.4 11.4 0 0 0 3.6.57 1 1 0 0 1 1 1V20a1 1 0 0 1-1 1A17 17 0 0 1 3 4a1 1 0 0 1 1-1h3.5a1 1 0 0 1 1 1c0 1.25.2 2.45.57 3.6a1 1 0 0 1-.25 1z"/></svg>
          214 555 0148
        </li>
        <li>
          <svg viewBox="0 0 24 24" aria-hidden="true"><circle cx="12" cy="12" r="4" fill="none" stroke="#fff" stroke-width="2.4"/><path d="M16 8v5a2.5 2.5 0 0 0 5 0v-1a9 9 0 1 0-3.5 7.1" fill="none" stroke="#fff" stroke-width="2.4"/></svg>
          mara@kestreldataworks.com
        </li>
        <li>
          <svg viewBox="0 0 24 24" aria-hidden="true"><g fill="none" stroke="#fff" stroke-width="2"><circle cx="12" cy="12" r="9"/><ellipse cx="12" cy="12" rx="4" ry="9"/><path d="M3 12h18"/></g></svg>
          www.kestreldataworks.com
        </li>
        <li>
          <svg viewBox="0 0 24 24" aria-hidden="true"><path fill="#fff" d="M12 3 2 12h3v9h5v-6h4v6h5v-9h3z"/></svg>
          Address line1, Address line2
        </li>
      </ul>
    </div>

    <div class="holder">
      <p class="holder-name">Mara Ellison</p>
      <p class="holder-role">Northfield Consulting</p>
    </div>
  </section>
</body>
</html>
```